Values Statement poster template

We want to develop a poster template for our company policies and statements which promote our company values in our workplaces.
These documents are important in showing our clients, suppliers and employees who we are and what we stand for.
The graphic design will incorporate our company logo, and be bright, uplifting and inspiring, developing a graphic theme that we can utilise for other company documents. The design will graphically illustrate and support our values statement, with colour and modern design.
This values poster will be the first in a series of documents using the same theme.The format will be a4 and a3 portrait
We are an environmental service business specialising in rehabilitation and revegetation

Target Market(s)

Tier one clients in industry, Mining, Construction and agriculture

Font styles to use
Other font styles liked:
• calibri

Requirements
Must have
• Professional , high end feel, able to read clearly on a poster
Nice to have
• graphic design elements, symbols, etc which support the message, that can be carried through to various documents such as quality, environmental, safety policies
A bright theme which ties in with our logo colours.

```html
<!DOCTYPE html>
<html lang="en">
<head>
<meta charset="utf-8">
<title>Our Values – Verdanta</title>
<link href="https://fonts.googleapis.com/css2?family=Arimo:wght@400;700&family=Bebas+Neue&display=swap" rel="stylesheet">
<style>
  :root {
    --page-bg: #e8e9eb;
    --paper: #ffffff;
    --green-dark: #0c6e38;
    --green-mid: #1f8a3f;
    --green-light: #6dbb45;
    --lime: #8cc63f;
    --text: #1c1c1c;
    --rule: #e6e6e6;
    --sky: #f1c257;
    --field: #5e7d1f;
    --orange: #f08a24;
  }
  * { box-sizing: border-box; margin: 0; padding: 0; }
  html, body { width: 1200px; height: 1021px; overflow: hidden; }
  body {
    background: var(--page-bg);
    font-family: "Arimo", Arial, sans-serif;
    color: var(--text);
    position: relative;
  }
  .poster {
    position: absolute; left: 250px; top: 18px;
    width: 700px; height: 985px;
    background: var(--paper);
    overflow: hidden;
  }
  .poster-art { position: absolute; inset: 0; }
  .brand {
    position: absolute; left: 47px; top: 32px;
    display: flex; align-items: center; gap: 8px;
  }
  .brand-dot { width: 18px; height: 18px; border-radius: 50%; background: var(--green-light); }
  .brand-name { font-weight: 700; font-size: 26px; color: var(--green-mid); letter-spacing: .2px; }

  .hero-title {
    position: absolute; left: 88px; top: 160px;
    font-family: "Bebas Neue", "Oswald", sans-serif;
    font-size: 84px; line-height: 70px; color: #fff;
    letter-spacing: 1px;
  }
  .hero-sub {
    position: absolute; left: 88px; top: 322px; width: 230px;
    font-size: 16px; line-height: 23.5px; color: #fff;
  }

  .value { position: absolute; }
  .value-head { display: flex; align-items: center; gap: 10px; margin-bottom: 12px; }
  .value-icon { flex: 0 0 auto; width: 30px; height: 30px; border-radius: 50%; }
  .value-title { font-size: 13px; line-height: 16.5px; font-weight: 700; color: #111; }
  .value-title span { font-weight: 400; display: block; }
  .value-title.accent { color: var(--green-mid); }
  .value p, .value li { font-size: 9.6px; line-height: 15px; }
  .value ul { list-style: none; }
  .value li { position: relative; padding-left: 9px; }
  .value li::before { content: "•"; position: absolute; left: 0; }
  .rule { position: absolute; height: 1px; background: var(--rule); }
</style>
</head>
<body>
<div class="poster">
  <svg class="poster-art" viewBox="0 0 700 985" width="700" height="985" aria-hidden="false">
    <defs>
      <linearGradient id="fieldTone" x1="0" y1="0" x2="0" y2="1">
        <stop offset="0" stop-color="#f0c35a"/>
        <stop offset=".3" stop-color="#d9b24e"/>
        <stop offset=".42" stop-color="#8fa63a"/>
        <stop offset=".7" stop-color="#6f8c24"/>
        <stop offset="1" stop-color="#3f5c14"/>
      </linearGradient>
      <linearGradient id="cardTone" x1="0" y1="0" x2="1" y2="1">
        <stop offset="0" stop-color="#0b6a35"/>
        <stop offset=".55" stop-color="#1f8a3f"/>
        <stop offset="1" stop-color="#5eb447"/>
      </linearGradient>
      <linearGradient id="footTone" x1="0" y1="0" x2="1" y2="0">
        <stop offset="0" stop-color="#8cc63f"/>
        <stop offset=".5" stop-color="#3da045"/>
        <stop offset="1" stop-color="#0c6e38"/>
      </linearGradient>
    </defs>
    <polygon points="0,88 700,34 700,39 0,97" fill="var(--green-light)"/>
    <polygon points="0,96 700,40 700,381 0,430" fill="url(#fieldTone)" role="img" aria-label="Photograph of a green grass field under a golden sunset sky with trees on the horizon"/>
    <polygon points="320,412 700,380 700,387 320,419" fill="var(--lime)"/>
    <path d="M47,172 Q47,108 112,104 L321,100 L321,410 L47,444 Z" fill="url(#cardTone)"/>
    <polygon points="0,972 700,920 700,985 0,985" fill="url(#footTone)"/>
    <polygon points="0,968 150,985 0,985" fill="var(--lime)"/>
  </svg>

  <div class="brand"><span class="brand-dot"></span><span class="brand-name">Verdanta</span></div>

  <h1 class="hero-title">Our<br>Values</h1>
  <p class="hero-sub">These are the things we value most, they define the way we do business</p>

  <!-- Column one -->
  <section class="value" style="left:45px; top:468px; width:185px;">
    <div class="value-head">
      <div class="value-icon" style="background:#f3a23a" role="img" aria-label="Icon of a group of people"></div>
      <h2 class="value-title">We value our people<span>above everything else.</span></h2>
    </div>
    <p>We demonstrate this by:</p>
    <ul>
      <li>Providing safe, positive, enjoyable workplaces where everyone feels valued and respected</li>
      <li>Providing Careers, not Jobs, we grow together</li>
      <li>Encouraging inclusion, participation and collaboration</li>
      <li>Recognising and rewarding contribution and excellence</li>
      <li>Supporting our people through tough times</li>
    </ul>
  </section>
  <div class="rule" style="left:45px; top:705px; width:180px;"></div>

  <section class="value" style="left:45px; top:722px; width:185px;">
    <div class="value-head">
      <div class="value-icon" style="background:#6dbb45" role="img" aria-label="Icon of a seedling growing from soil"></div>
      <h2 class="value-title">We do good things<span>for the planet</span></h2>
    </div>
    <p>Our products are helping revegetate Australia, which we are tremendously proud of. We minimise our environmental impact in everything we do.</p>
  </section>
  <div class="rule" style="left:45px; top:839px; width:180px;"></div>

  <section class="value" style="left:45px; top:858px; width:185px;">
    <div class="value-head">
      <div class="value-icon" style="background:#e8455a" role="img" aria-label="Icon of a hand holding a heart"></div>
      <h2 class="value-title accent">We give back</h2>
    </div>
    <p>We appreciate our success and we give back by supporting our community, and those less fortunate.</p>
  </section>

  <!-- Column two -->
  <section class="value" style="left:259px; top:459px; width:185px;">
    <div class="value-head">
      <div class="value-icon" style="background:var(--orange)" role="img" aria-label="Icon of an award ribbon"></div>
      <h2 class="value-title">We set the standard</h2>
    </div>
    <ul>
      <li>We are uncompromising on quality</li>
      <li>We are the best at what we do, and we do what we are best at</li>
      <li>We are always improving</li>
      <li>We are pioneering</li>
    </ul>
  </section>
  <div class="rule" style="left:259px; top:580px; width:180px;"></div>

  <section class="value" style="left:259px; top:597px; width:185px;">
    <div class="value-head">
      <svg class="value-icon" viewBox="0 0 30 30" width="30" height="30" aria-hidden="true" style="border-radius:0">
        <path d="M15,2 L27,6 V14 C27,21 21,26 15,28 C9,26 3,21 3,14 V6 Z" fill="var(--green-light)"/>
        <circle cx="15" cy="15" r="6.5" fill="#fff"/>
        <path d="M11.8,15.2 L14.2,17.5 L18.4,12.8" fill="none" stroke="var(--green-light)" stroke-width="1.8"/>
      </svg>
      <h2 class="value-title">Our workplaces<br>are safe</h2>
    </div>
    <p>There is nothing more important to us than our people going home healthy and safe every day. We won't accept anything less. We believe safety is a management choice. By providing safe work systems, and education we achieve our daily goal of Zero Harm. At Verdanta we;</p>
    <ul>
      <li>Take the time to make our work areas safe, whatever it takes</li>
      <li>Don't accept shortcuts</li>
      <li>Look out for each other</li>
      <li>Investigate our incidents and learn from them, we won't accept repeats</li>
      <li>Are constantly looking for ways to improve the safety of our workplaces.</li>
      <li>Think safe, work safer, go home safe!</li>
    </ul>
  </section>

  <!-- Column three -->
  <section class="value" style="left:473px; top:422px; width:182px;">
    <div class="value-head">
      <div class="value-icon" style="background:#f6b93b" role="img" aria-label="Icon of raised hands"></div>
      <h2 class="value-title">We are proud of<br>who we are</h2>
    </div>
    <p>Our reputation means the world to us. We:</p>
    <ul>
      <li>Treat everyone with respect and we expect it in return</li>
      <li>Follow the rules</li>
      <li>Do what we say we will do</li>
      <li>Own our mistakes and we fix them</li>
      <li>Are trustworthy and transparent</li>
    </ul>
  </section>
  <div class="rule" style="left:473px; top:599px; width:180px;"></div>

  <section class="value" style="left:473px; top:617px; width:182px;">
    <div class="value-head">
      <div class="value-icon" style="background:#6dbb45; border-radius:3px" role="img" aria-label="Icon of steps with a flag on top"></div>
      <h2 class="value-title">We succeed together</h2>
    </div>
    <p>We believe in win-win relationships. When our business is profitable everyone benefits, our owners, employees, clients and the community. At Verdanta we:</p>
    <ul>
      <li>Work as a team, we get it done together</li>
      <li>We treat our suppliers and subcontractors like they are part of the team.</li>
      <li>Are building on our success, and growing together</li>
      <li>Choose to work with employees, customers and suppliers who fit our values</li>
    </ul>
  </section>
</div>
</body>
</html>
```